5 Planner Covers for Teacher Planners

Hello,
I currently run a Speech-Language Pathologist website and have created a planner for my fellow Speech Therapist. I would like someone to create 5 different planner covers so my followers will have different options to choose from.
Here is my planner from last year to give you an idea of what the planner will look like http://www.talkbloomshop.example/free-slp-planner/
My followers are mostly women aged 25-50. However, I don't want the covers to be overly girly or excessive with flowers. Simple is better.
I'd also like there to be an editable text box to allow the Speech Therapist to type their name on their cover if they wish.
Planner Cover can say any of the following: SLP Planner, Planner, Speech Therapy Planner, Speech-Language Pathologist (maybe this title could be editable as well??).
To give you an idea I have uploaded a screenshot of last year's planners cover that I made myself.
What I am looking for:
-Size 8.5" by 11"
-5 different planner covers
-1 gender-neutral cover
-simple design
-limited flowers (or overly girly
-text box to add a personal name
-Possible titles: SLP Planner, Planner, Speech Therapy Planner, Speech-Language Pathologist (maybe this title could be editable as well??)
Target Market(s)
Women aged 25-50
Colors
Designer to choose colors to be used in the design.
Requirements
Must have
- What I am looking for:
-Size 8.5" by 11"
-1 gender-neutral cover
-simple design
Nice to have
- I've uploaded some that I like from Craftora to give you an idea.
Here is my craftora store https://www.craftora.example/shop/QuietMeadowHome to give you an idea of things I like.
I like Marla Pendry and her simple elegant rustic style.

```html
<!DOCTYPE html>
<html lang="en">
<head>
<meta charset="utf-8">
<title>SLP Planner Covers</title>
<link rel="stylesheet" href="https://fonts.googleapis.com/css2?family=Playfair+Display:wght@500;600&family=Great+Vibes&family=Questrial&family=Oswald:wght@400&family=Almendra:wght@700&display=swap">
<style>
  :root {
    --page: #f1ebe2;
    --ink: #111111;
    --cream: #fdfbd2;
    --gold: #c3a153;
    --plum: #9c2f86;
    --pink: #e77db1;
    --mint: #8fd3b2;
    --lavender: #cf9ede;
    --lavender-soft: #dcb6e6;
    --white: #ffffff;
    --slate: #3a3a3a;
    --teal: #3f8f8c;
    --rose: #e04f7e;
  }
  * { box-sizing: border-box; margin: 0; padding: 0; }
  html, body { width: 1200px; height: 1018px; overflow: hidden; background: var(--page); }
  .canvas { position: relative; width: 1200px; height: 1018px; }

  .cover {
    position: absolute; width: 328px; height: 424px; overflow: hidden;
    box-shadow: 0 6px 18px rgba(0,0,0,.18);
  }
  .cover--marble-watercolor { left: 80px;  top: 68px; }
  .cover--cream-floral      { left: 436px; top: 68px; background: var(--cream); }
  .cover--lavender-wood     { left: 792px; top: 68px; }
  .cover--arrow-stripe      { left: 258px; top: 526px; }
  .cover--marble-rose       { left: 614px; top: 526px; }

  .art, .fill { position: absolute; }
  .art--bouquet { border-radius: 18px; opacity: .85; }

  .title-slp {
    position: absolute; left: 0; right: 0; text-align: center;
    font-family: "Playfair Display", serif; font-weight: 600;
    font-size: 76px; line-height: 1; color: var(--ink); letter-spacing: -1px;
  }
  .title-planner {
    position: absolute; left: 0; right: 0; text-align: center;
    font-family: "Great Vibes", cursive; font-size: 78px; line-height: 1;
    color: var(--ink); -webkit-text-stroke: 1.2px var(--ink);
    transform: rotate(-8deg);
  }

  .owner-box { position: absolute; text-align: center; }
  .owner-this {
    font-family: "Questrial", sans-serif; font-size: 13px; line-height: 18px;
    letter-spacing: .5px; color: var(--ink);
  }
  .owner-belongs { font-family: "Oswald", sans-serif; font-size: 11px; color: var(--gold); margin-top: 2px; }
  .owner-first { font-family: "Great Vibes", cursive; font-size: 24px; line-height: 1; color: var(--plum); }
  .owner-last {
    font-family: "Questrial", sans-serif; font-size: 22px; line-height: 1; color: var(--gold); letter-spacing: 1px;
  }
  .owner-rule { border-bottom: 1px dashed #8a8a8a; margin: 4px 6px 0; }
  .belongs-script {
    position: absolute; left: 0; right: 0; text-align: center;
    font-family: "Great Vibes", cursive; font-size: 17px; color: #2b2b4a;
  }
  .belongs-bold {
    position: absolute; left: 0; right: 0; text-align: center;
    font-family: "Almendra", serif; font-weight: 700; font-size: 14px; color: var(--ink);
    text-shadow: 0 0 3px #fff, 0 0 2px #fff;
  }
  .name-oval {
    position: absolute; border-radius: 50%; background: var(--white);
    display: flex; flex-direction: column; align-items: center; justify-content: center;
  }
</style>
</head>
<body>
<main class="canvas">

  <section class="cover cover--marble-watercolor">
    <div class="art" role="img" aria-label="White marble texture with pink and blue watercolour wash"
      style="inset:0;background:linear-gradient(160deg,#eceeef 0%,#e6c9cf 30%,#c3deec 52%,#e9ecee 78%,#eef0f1 100%);"></div>
    <div class="fill" style="left:96px;top:0;width:136px;height:27px;background:var(--cream);border-bottom:2px solid #e8b7b0;"></div>
    <svg class="fill" width="328" height="424" style="left:0;top:0">
      <rect x="50" y="98" width="225" height="224" fill="none" stroke="#fff" stroke-width="3.5"/>
      <rect x="64" y="111" width="199" height="196" fill="none" stroke="#fff" stroke-width="3.5"/>
    </svg>
    <div class="fill" style="left:96px;top:194px;width:136px;height:230px;background:var(--cream);border-top:2px solid #e8b7b0;"></div>
    <div class="fill" style="left:103px;top:204px;width:121px;height:176px;border:1px solid #ecc3bb;"></div>
    <div class="title-slp" style="top:36px;">SLP</div>
    <div class="title-planner" style="top:130px;left:-6px;">Planner</div>
    <div class="owner-box" style="left:103px;top:222px;width:121px;">
      <div class="owner-this">THIS<br>PLANNER</div>
      <div class="owner-belongs">Belongs To:</div>
      <div class="owner-first" style="margin-top:12px;">Rosalyn</div>
      <div class="owner-last">HAYES</div>
      <div class="owner-rule"></div>
    </div>
    <div class="art art--bouquet" role="img" aria-label="Small watercolour bouquet of roses and feathers"
      style="left:120px;top:344px;width:90px;height:58px;background:linear-gradient(120deg,#d8c3b0,#eea2bf 50%,#c9a6d6);"></div>
  </section>

  <section class="cover cover--cream-floral">
    <div class="art" role="img" aria-label="Watercolour band of coral flowers and green leaves"
      style="left:0;top:0;width:328px;height:78px;background:linear-gradient(90deg,#cfdcb9,#f2b9a3 30%,#d7e0bf 55%,#f1a992 80%,#cfdcb9);border-radius:0 0 40% 40% / 0 0 30px 30px;opacity:.85;"></div>
    <svg class="fill" width="328" height="424" style="left:0;top:0">
      <path d="M90 115 H39 V344 H102 M226 344 H290 V115 H238" fill="none" stroke="var(--mint)" stroke-width="1.5"/>
    </svg>
    <div class="title-slp" style="top:80px;">SLP</div>
    <div class="title-planner" style="top:148px;">Planner</div>
    <div class="belongs-script" style="top:240px;">This Planner Belongs To:</div>
    <div class="name-oval" style="left:102px;top:275px;width:124px;height:86px;border:1.5px solid var(--mint);">
      <div class="owner-first" style="color:#3b3b55;font-size:20px;">Rosalyn</div>
      <div class="owner-last" style="color:var(--pink);font-size:20px;">HAYES</div>
    </div>
    <div class="art" role="img" aria-label="Watercolour spray of coral roses and leaves"
      style="left:60px;top:372px;width:208px;height:60px;border-radius:50% 50% 0 0;background:linear-gradient(90deg,#cfdcb9,#f0a28a 50%,#cfdcb9);opacity:.85;"></div>
  </section>

  <section class="cover cover--lavender-wood">
    <div class="art" role="img" aria-label="Lavender painted rustic wood planks fading to white"
      style="inset:0;background:linear-gradient(180deg,var(--lavender) 0%,#d9b3e2 55%,#f6eef8 100%);"></div>
    <svg class="fill" width="328" height="424" style="left:0;top:0">
      <rect x="32" y="32" width="265" height="360" fill="none" stroke="var(--gold)" stroke-width="1.2" stroke-dasharray="2 1.5"/>
    </svg>
    <div class="fill" style="left:96px;top:0;width:136px;height:198px;background:#0d0d0d;"></div>
    <div class="fill" style="left:106px;top:54px;width:116px;height:132px;border:1px solid var(--gold);"></div>
    <div class="art art--bouquet" role="img" aria-label="Small watercolour bouquet of roses and feathers"
      style="left:128px;top:30px;width:72px;height:46px;background:linear-gradient(120deg,#c9b7a6,#e886b5 50%,#b78fd0);"></div>
    <div class="title-slp" style="left:96px;right:auto;width:136px;top:92px;font-size:50px;color:var(--white);font-weight:500;">SLP</div>
    <div class="title-planner" style="left:96px;right:auto;width:136px;top:140px;font-size:38px;color:var(--white);-webkit-text-stroke:.6px var(--white);">Planner</div>
    <div class="belongs-bold" style="top:238px;">This Planner Belongs To:</div>
    <div class="name-oval" style="left:52px;top:281px;width:98px;height:70px;border:1px dashed var(--gold);">
      <div class="owner-first" style="color:#3b3b55;font-size:19px;">Rosalyn</div>
      <div class="owner-last" style="color:#8e2a86;font-size:19px;">HAYES</div>
    </div>
    <div class="art art--bouquet" role="img" aria-label="Watercolour cluster of roses, pansies and feathers"
      style="left:150px;top:300px;width:150px;height:100px;border-radius:50px;background:linear-gradient(120deg,#c9b7a6,#e886b5 45%,#b9e0c8 75%,#a992c9);"></div>
  </section>

  <section class="cover cover--arrow-stripe">
    <div class="art" role="img" aria-label="Pattern of watercolour arrows and feathers on cream with lavender edges"
      style="inset:0;background:linear-gradient(90deg,var(--lavender) 0%,#f3e5c9 10%,var(--cream) 18%,#eef0d6 50%,var(--cream) 82%,#f3e5c9 90%,var(--lavender) 100%);"></div>
    <div class="fill" style="left:95px;top:0;width:136px;height:27px;background:var(--white);border-bottom:3px solid var(--lavender-soft);"></div>
    <div class="fill" style="left:95px;top:194px;width:136px;height:230px;background:var(--white);border-top:3px solid var(--lavender-soft);"></div>
    <div class="fill" style="left:103px;top:204px;width:121px;height:176px;border:1px solid var(--lavender-soft);"></div>
    <div class="title-slp" style="top:36px;">SLP</div>
    <div class="title-planner" style="top:110px;left:-6px;">Planner</div>
    <div class="owner-box" style="left:103px;top:222px;width:121px;">
      <div class="owner-this">THIS<br>PLANNER</div>
      <div class="owner-belongs">Belongs To:</div>
      <div class="owner-first" style="margin-top:12px;">Rosalyn</div>
      <div class="owner-last">HAYES</div>
      <div class="owner-rule"></div>
    </div>
    <div class="art art--bouquet" role="img" aria-label="Small watercolour bouquet of pink and yellow flowers with leaves"
      style="left:113px;top:348px;width:100px;height:52px;background:linear-gradient(120deg,#b9d59c,#ee8fb5 50%,#f4dc8a);"></div>
  </section>

  <section class="cover cover--marble-rose">
    <div class="art" role="img" aria-label="White and grey marble texture"
      style="inset:0;background:linear-gradient(135deg,#f1f1f1 0%,#dcdcdc 35%,#f4f4f4 60%,#d6d6d6 100%);"></div>
    <div class="art" role="img" aria-label="Watercolour pink rose with teal leaves and gold outline leaves"
      style="left:0;top:0;width:150px;height:110px;border-radius:0 0 100% 0;background:linear-gradient(135deg,var(--rose) 0%,#e986a8 35%,var(--teal) 75%);opacity:.85;"></div>
    <div class="art" role="img" aria-label="Watercolour pink rose with teal leaves and gold outline leaves"
      style="left:190px;top:314px;width:138px;height:110px;border-radius:100% 0 0 0;background:linear-gradient(315deg,var(--rose) 0%,#e986a8 35%,var(--teal) 75%);opacity:.85;"></div>
    <div class="title-slp" style="top:52px;">SLP</div>
    <div class="title-planner" style="top:120px;left:8px;">Planner</div>
    <div class="fill" style="left:95px;top:203px;width:137px;height:151px;background:var(--cream);"></div>
    <div class="fill" style="left:103px;top:211px;width:121px;height:135px;border:1px solid var(--gold);"></div>
    <div class="owner-box" style="left:103px;top:220px;width:121px;">
      <div class="owner-this">THIS<br>PLANNER</div>
      <div class="owner-belongs">Belongs To:</div>
      <div class="owner-first" style="margin-top:12px;">Rosalyn</div>
      <div class="owner-last" style="color:var(--slate);">HAYES</div>
      <div class="owner-rule"></div>
    </div>
  </section>

</main>
</body>
</html>
```